Bright And Steady Web Design & Marketing

Will award a 2nd place prize of $100.00 if someone can come up with a logo to match this design!
Updates

Okay, I'm really looking to see some better designs here. What do you think will bring the best designs out? Please remember with all future submissions I'm looking for a cartoon style / illustrator style website. I'm not sure what the technical term is for it, so I uploaded some images in the brief.

Target Market(s)

Small Business Owners

Industry/Entity Type

Marketing

Logo Text

BrightAndSteady.example

Number of Pages Required

1 page

Colors

Designer to choose colors to be used in the design.

Requirements
Must have
• Logo should say BrightAndSteady.example I would like more than just a text logo. I want some sort of cool custom graphic / icon with it that will look nice on shirts/hats/etc

```html
<!DOCTYPE html>
<html lang="en">
<head>
<meta charset="utf-8">
<title>Bright And Steady Web Design &amp; Marketing</title>
<link rel="stylesheet" href="https://fonts.googleapis.com/css2?family=Jost:wght@400;500;600;700&family=Didact+Gothic&display=swap">
<style>
:root{
  --navy:#2e4a8e;
  --royal:#2f2fe0;
  --band:#3d3df2;
  --green:#6ab04c;
  --news:#6db55a;
  --footer:#3e5b9b;
  --grey:#efefef;
  --white:#ffffff;
  --ink:#2c3f7a;
  --muted:#6f7790;
}
*{box-sizing:border-box;margin:0;padding:0}
html,body{width:1200px;height:2812px;overflow:hidden;background:var(--white)}
body{font-family:"Didact Gothic",sans-serif;color:var(--ink)}
.canvas{position:relative;width:1200px;height:2812px;overflow:hidden}
.abs{position:absolute}
.center{left:0;width:1200px;text-align:center}

/* header */
.site-header{top:0;left:0;width:1200px;height:53px;background:var(--white)}
.brand{left:161px;top:9px;font-family:"Jost",sans-serif;font-weight:600;font-size:30px;letter-spacing:2px;color:var(--navy)}
.main-nav{right:160px;top:18px;display:flex;gap:30px;font-size:14px;color:#3a3a4a}

/* hero */
.hero{top:53px;left:0;width:1200px;height:453px;background:radial-gradient(ellipse at center,#2b2bea 0%,#2424d8 55%,#3c5fb0 100%)}
.hero-title{top:208px;font-family:"Jost",sans-serif;font-weight:500;font-size:34px;line-height:40px;letter-spacing:1px;color:var(--white);text-transform:uppercase}
.btn-outline{left:482px;top:322px;width:240px;height:49px;border:2px solid var(--white);color:var(--white);font-family:"Jost",sans-serif;font-weight:500;font-size:16px;display:flex;align-items:center;justify-content:center;letter-spacing:.5px}

/* services */
.services-title{top:570px;font-family:"Jost",sans-serif;font-weight:600;font-size:35px;letter-spacing:3px;color:var(--navy)}
.services-title span{color:var(--green)}
.service{width:220px;text-align:center}
.service-icon{display:block;margin:0 auto 10px;width:52px;height:52px;border-radius:12px;background:var(--green)}
.service-name{font-family:"Jost",sans-serif;font-weight:500;font-size:18px;line-height:21px;color:var(--navy)}

/* about */
.about{top:1031px;left:0;width:1200px;height:343px;background:var(--grey)}
.label{font-family:"Jost",sans-serif;font-weight:600;font-size:12px;letter-spacing:1px;color:var(--ink);text-transform:uppercase}
.about-lead{top:1134px;left:180px;width:840px;text-align:center;font-family:"Jost",sans-serif;font-weight:500;font-size:18.5px;line-height:26px;color:var(--ink)}
.about-note{top:1232px;font-size:13px;color:var(--muted)}
.btn-solid{left:546px;top:1283px;width:108px;height:37px;background:var(--navy);color:var(--white);border-radius:3px;font-family:"Jost",sans-serif;font-weight:600;font-size:11px;letter-spacing:.5px;display:flex;align-items:center;justify-content:center}

/* difference band */
.diff{top:1374px;left:0;width:1200px;height:404px;background:linear-gradient(120deg,#3a3aef 0%,#4343f5 50%,#3a3aec 100%)}
.diff-title{left:161px;top:1492px;width:420px;white-space:nowrap;font-family:"Jost",sans-serif;font-weight:600;font-size:39px;line-height:44px;letter-spacing:3px;color:var(--white)}
.diff-title span{color:var(--green)}
.diff-sub{left:161px;top:1563px;font-family:"Jost",sans-serif;font-weight:600;font-size:19px;letter-spacing:.5px;color:#9de04a}
.diff-text{left:161px;top:1600px;width:420px;font-family:"Jost",sans-serif;font-weight:500;font-size:13.5px;line-height:18px;color:var(--white)}
.divider-v{left:600px;top:1425px;height:319px;border-left:2px dashed rgba(255,255,255,.8)}
.divider-h{left:638px;top:1600px;width:397px;border-top:2px dashed rgba(255,255,255,.8)}
.feature{width:210px;color:var(--white)}
.feature-icon{width:38px;height:38px;border-radius:50%;background:rgba(255,255,255,.9);margin-bottom:10px}
.feature h3{font-family:"Jost",sans-serif;font-weight:600;font-size:14px;margin-bottom:4px}
.feature p{font-size:12px;line-height:14px}
.contact-line{display:flex;align-items:center;gap:10px;color:var(--white);font-family:"Jost",sans-serif;font-weight:500;font-size:14px}

/* team */
.team-photo{left:207px;top:1866px;width:262px;height:262px;border-radius:50%;background:radial-gradient(circle at 60% 45%,#e9e4df 0%,#d9d4cf 55%,#b8b2ae 100%)}
.team-quote{top:1908px;left:581px;width:470px;text-align:center;font-family:"Jost",sans-serif;font-weight:500;font-size:14.5px;line-height:24px;color:var(--ink)}
.team-name{top:2020px;left:581px;width:470px;text-align:center;font-size:14px;color:var(--green)}
.team-role{top:2043px;left:581px;width:470px;text-align:center;font-size:14px;color:var(--muted)}
.pager{display:flex;gap:10px}
.pager span{width:27px;height:27px;border-radius:3px;display:flex;align-items:center;justify-content:center}
.pager .on{background:var(--navy)}
.pager .off{border:1.5px solid #9aa0b0;background:var(--white)}
.pager .light{border:2px solid var(--white)}

/* news */
.news{top:2213px;left:0;width:1200px;height:262px;background:var(--news)}
.news-label{top:2257px;color:var(--white)}
.news-text{top:2298px;left:180px;width:840px;text-align:center;font-family:"Jost",sans-serif;font-weight:500;font-size:14.5px;line-height:26px;color:var(--white)}
.news-meta{top:2361px;font-size:13px;color:#d8f0c8}
.news-meta b{color:var(--white);font-family:"Jost",sans-serif;font-weight:600}

/* footer */
.footer{top:2475px;left:0;width:1200px;height:337px;background:var(--footer)}
.footer-text{color:var(--white)}
.f-head{font-family:"Jost",sans-serif;font-weight:600;font-size:10px;letter-spacing:.4px;text-transform:uppercase;color:var(--white)}
.f-body{font-size:11px;line-height:12px;color:var(--white)}
.f-list{list-style:none;font-size:11px;line-height:22.5px;color:var(--white)}
.f-list li::before{content:"- "}
.f-link{font-size:11px;text-decoration:underline;line-height:28px;color:var(--white)}
.f-services{left:698px;top:2532px;font-family:"Jost",sans-serif;font-weight:500;font-size:36px;line-height:38px;letter-spacing:3px;color:var(--white)}
.f-para{left:698px;width:360px;font-size:11px;line-height:15px;color:var(--white)}
.f-strong{left:698px;top:2697px;font-family:"Jost",sans-serif;font-weight:600;font-size:11.5px;text-decoration:underline;color:var(--white)}
.f-rule{left:161px;top:2760px;width:878px;border-top:1px solid rgba(255,255,255,.25)}
.copyright{left:161px;top:2783px;font-size:11px;color:var(--white)}
.payments{right:161px;top:2776px;display:flex;align-items:center;gap:8px;font-size:11px;color:var(--white)}
.card{width:34px;height:22px;background:var(--white);border-radius:2px}
</style>
</head>
<body>
<div class="canvas">

  <header class="site-header abs">
    <div class="brand abs">BRIGHT &amp; STEADY</div>
    <nav class="main-nav abs">
      <span>Home</span><span>About Us</span><span>Services &amp; Pricing</span><span>Our Team</span><span>Portfolio</span><span>Contact Us</span>
    </nav>
  </header>

  <section class="hero abs" role="img" aria-label="Bold blue backdrop with large green and yellow chevron shapes"></section>
  <h1 class="hero-title abs center">The Design &amp; Marketing Team That<br>Always Puts Bright &amp; Steady Before Profits</h1>
  <div class="btn-outline abs">CONTACT US NOW</div>

  <h2 class="services-title abs center">BRIGHTANDSTEADY <span>SERVICES</span></h2>
  <div class="service abs" style="left:124px;top:653px"><span class="service-icon" role="img" aria-label="Website design icon"></span><div class="service-name">Website Design &amp;<br>Management</div></div>
  <div class="service abs" style="left:355px;top:653px"><span class="service-icon" role="img" aria-label="Logo design icon"></span><div class="service-name">Logo Design &amp;<br>Branding Materials</div></div>
  <div class="service abs" style="left:614px;top:653px"><span class="service-icon" role="img" aria-label="Online store icon"></span><div class="service-name">Online Store Design<br>&amp; Management</div></div>
  <div class="service abs" style="left:854px;top:653px"><span class="service-icon" role="img" aria-label="Local SEO icon"></span><div class="service-name">Local<br>SEO Management</div></div>
  <div class="service abs" style="left:124px;top:840px"><span class="service-icon" role="img" aria-label="Search engine optimization icon"></span><div class="service-name">Search Engine<br>Optimization</div></div>
  <div class="service abs" style="left:355px;top:840px"><span class="service-icon" role="img" aria-label="Social media icon"></span><div class="service-name">Social Media<br>Marketing</div></div>
  <div class="service abs" style="left:614px;top:840px"><span class="service-icon" role="img" aria-label="Marketing megaphone icon"></span><div class="service-name">Marketing Material<br>&amp; Print Design</div></div>
  <div class="service abs" style="left:854px;top:840px"><span class="service-icon" role="img" aria-label="Outsourcing icon"></span><div class="service-name">Outsourcing<br>Management</div></div>

  <section class="about abs"></section>
  <div class="label abs center" style="top:1085px">About Us</div>
  <p class="about-lead abs">We believe that honesty and integrity come before personal profits. We are a family owned and operated company. Our parents raised us to take care of each other and that's exactly what we've done. We treat each of our clients with the same loyalty and respect that we give each other.</p>
  <p class="about-note abs center">We are not looking to have hundreds and hundreds of clients. We are looking to expand our family with a handful...</p>
  <div class="btn-solid abs">LEARN MORE</div>

  <section class="diff abs" role="img" aria-label="Blue backdrop with faint chevron shapes"></section>
  <div class="diff-title abs">BRIGHT <span>&amp;</span> STEADY</div>
  <div class="diff-sub abs">WHAT MAKES ME DIFFERENT?</div>
  <p class="diff-text abs">Lorem ipsum dolor sit amet, consectetur adipiscing elit, sed do eiusmod tempor incididunt ut labore et dolore magna aliqua. Ut enim ad minim veniam, quis nostrud exercitation ullamco laboris nisi ut aliquip ex ea commodo consequat.</p>
  <div class="divider-v abs"></div>
  <div class="feature abs" style="left:638px;top:1440px"><div class="feature-icon" role="img" aria-label="Money in hand icon"></div><h3>100% Risk Free Investment</h3><p>If we are unable to deliver anything that we say we can we will refund you 100% of your investment.</p></div>
  <div class="feature abs" style="left:872px;top:1440px"><div class="feature-icon" role="img" aria-label="Customer icon"></div><h3>Customer Loyalty Program</h3><p>After 12 months of on time payments - Customers will receive cash back reward bonuses</p></div>
  <div class="divider-h abs"></div>
  <div class="feature abs" style="left:638px;top:1637px"><div class="feature-icon" role="img" aria-label="Around the clock support icon"></div><h3 style="font-size:13px">24/7 U.S. Based Customer</h3></div>
  <div class="contact-line abs" style="left:853px;top:1657px">
    <svg width="18" height="14" viewBox="0 0 18 14"><rect x="1" y="1" width="16" height="12" rx="1" fill="none" stroke="#fff" stroke-width="1.6"/><path d="M1 2l8 6 8-6" fill="none" stroke="#fff" stroke-width="1.6"/></svg>info@brightandsteady.example</div>
  <div class="contact-line abs" style="left:853px;top:1690px">
    <svg width="18" height="18" viewBox="0 0 18 18"><circle cx="9" cy="9" r="8" fill="none" stroke="#fff" stroke-width="1.5"/><path d="M6 5c0 4 3 7 7 7l-1.5-2-1.5 .8c-1-.6-2-1.6-2.6-2.6l.8-1.5z" fill="#fff"/></svg>+001 555 0134</div>

  <div class="team-photo abs" role="img" aria-label="Portrait of the chief executive writing quality, service and reliability on glass"></div>
  <div class="label abs" style="top:1866px;left:581px;width:470px;text-align:center">Our Team</div>
  <p class="team-quote abs">Lorem ipsum dolor sit amet, consectetur adipiscing elit, sed do eiusmod tempor incididunt ut labore et dolore magna aliqua. Ut enim ad minim veniam, quis nostrud exercitation ullamco laboris nisi ut aliquip ex ea commodo consequat.</p>
  <div class="team-name abs">Daniel Morrow</div>
  <div class="team-role abs">Chief Executive Officer</div>
  <div class="pager abs" style="left:773px;top:2092px">
    <span class="on"><svg width="8" height="10"><path d="M7 0L0 5l7 5z" fill="#fff"/></svg></span>
    <span class="off"><svg width="8" height="10"><path d="M1 0l7 5-7 5z" fill="#5a6277"/></svg></span>
  </div>

  <section class="news abs"></section>
  <div class="label news-label abs center">Featured News</div>
  <p class="news-text abs">Lorem ipsum dolor sit amet, consectetur adipiscing elit, sed do eiusmod tempor incididunt ut labore et dolore magna aliqua. Ut enim ad minim veniam, quis nostrud exercitation ullamco laboris nisi ut aliquip...</p>
  <div class="news-meta abs center">Posted On : <b>2017-11-08</b> / BY : <b>Daniel Morrow</b> / IN Event</div>
  <div class="pager abs" style="left:565px;top:2405px">
    <span class="on"><svg width="8" height="10"><path d="M7 0L0 5l7 5z" fill="#fff"/></svg></span>
    <span class="light"><svg width="8" height="10"><path d="M1 0l7 5-7 5z" fill="#fff"/></svg></span>
  </div>

  <footer class="footer abs"></footer>
  <div class="f-head abs" style="left:161px;top:2505px">Contact Us</div>
  <p class="f-body abs" style="left:161px;top:2528px;width:160px">Lorem Ipsum Dolor Sit Amet Amet Consectetur Lorem Dolor Sit Amet Amet Dolor</p>
  <div class="f-head abs" style="left:381px;top:2505px">Navigations</div>
  <ul class="f-list abs" style="left:381px;top:2525px">
    <li>Home</li><li>About</li><li>Service</li><li>Pricing</li><li>Our Team</li><li>Clients</li><li>Portfolio</li><li>Contact Us</li>
  </ul>
  <div class="f-head abs" style="left:531px;top:2505px">Follow Us</div>
  <div class="abs" style="left:531px;top:2522px"><div class="f-link">Social Page</div><div class="f-link">News Feed</div></div>
  <div class="f-head abs" style="left:698px;top:2505px">Unmatched Personal Service</div>
  <div class="f-services abs">SERVICES</div>
  <p class="f-para abs" style="top:2582px">Do you need us to come to your office to help train staff on the management of your new website, content management system, or computer software?</p>
  <p class="f-para abs" style="top:2642px">That's not a problem. We will come to you and provide hands on training.</p>
  <div class="f-strong abs">Website Leasing, 90 Days Same As Cash, Website Financing</div>
  <div class="f-rule abs"></div>
  <div class="copyright abs">&copy; Copyright 2017 Bright And Steady. All Rights Reserved.</div>
  <div class="payments abs">Multiple Payment Options Available :<span class="card"></span><span class="card"></span><span class="card"></span></div>

</div>
</body>
</html>
```